Tavner's Produce Business Cards

A new style and great looking business cards for my parents business. Simple yet catchy and something that shows a home grown produce and apples farm!

Target Market(s)

Farmers market buyers, someone who loves home grown produce, fresh vegetables and apples.

Industry/Entity Type

Business

Requirements
Must have
• Tavner's Produce is the name, so that will have to be on the card. Also incorporate our logo! but maybe not exactly the same? Open to all ideas!

Marisela Tavner ( Owner)

Address: 42 Cedar Hollow Ln.
Fernridge, OR 97411

Phone: (509) 555-0147
Cell (509) 555-0183
Nice to have
• I have a logo that was done not too long ago using design! I would like to have parts of the logo be used, but I also want examples of NOT using the logo and see if we can get the family produce look too it!

```html
<!DOCTYPE html>
<html lang="en">
<head>
<meta charset="utf-8">
<title>Tavner's Produce Business Cards</title>
<link rel="stylesheet" href="https://fonts.googleapis.com/css2?family=Open+Sans:wght@400;600&family=Dosis:wght@600;700&family=Courier+Prime:wght@400;700&display=swap">
<style>
  :root {
    --page: #3a3a3a;
    --card-light: #e8d5a6;
    --card-dark: #d6bc84;
    --orange: #ef7a1a;
    --orange-deep: #e8650f;
    --amber: #f6b21c;
    --yellow: #f9cf3a;
    --brown-text: #8a4a1c;
    --label-white: #ffffff;
    --owner-grey: #f2ece0;
    --red: #e0392a;
    --mono-ink: #6b3418;
    --mono-name: #8b361c;
    --mono-role: #b4724c;
    --ghost: rgba(232, 140, 100, 0.22);
  }
  * { box-sizing: border-box; margin: 0; padding: 0; }
  html, body {
    width: 1200px;
    height: 900px;
    overflow: hidden;
    background: var(--page);
  }
  .stage {
    position: relative;
    width: 1200px;
    height: 900px;
  }
  .card {
    position: absolute;
    width: 750px;
    height: 412px;
    border-radius: 32px;
    overflow: hidden;
    background: linear-gradient(160deg, var(--card-light) 0%, var(--card-dark) 100%);
  }
  .card--color { left: 286px; top: 30px; }
  .card--type { left: 290px; top: 468px; height: 405px; }

  /* Colour card */
  .brand-mark {
    position: absolute;
    left: 30px;
    top: 18px;
    width: 186px;
    height: 170px;
    display: flex;
    flex-direction: column;
    align-items: center;
    justify-content: center;
    gap: 12px;
  }
  .brand-mark__dot {
    width: 46px;
    height: 46px;
    border-radius: 50%;
    background: var(--orange);
  }
  .brand-mark__name {
    font-family: "Open Sans", sans-serif;
    font-weight: 600;
    font-size: 24px;
    line-height: 1.15;
    text-align: center;
    color: var(--orange);
  }
  .tractor {
    position: absolute;
    left: 246px;
    top: 112px;
    width: 140px;
    height: 98px;
    border-radius: 18px;
    background: linear-gradient(180deg, #f08a2a, #e8700f);
  }
  .swoosh {
    position: absolute;
    left: 0;
    top: 0;
    width: 750px;
    height: 412px;
  }
  .contact {
    position: absolute;
    left: 0;
    top: 272px;
    display: grid;
    grid-template-columns: 111px auto;
    column-gap: 15px;
    row-gap: 2px;
    font-family: "Open Sans", sans-serif;
    font-size: 20px;
    line-height: 27px;
  }
  .contact__label { text-align: right; color: var(--label-white); }
  .contact__value { color: var(--brown-text); }
  .person {
    position: absolute;
    left: 464px;
    width: 250px;
    top: 284px;
    text-align: center;
  }
  .person__name {
    font-family: "Dosis", sans-serif;
    font-weight: 700;
    font-size: 37px;
    line-height: 1;
    white-space: nowrap;
    color: var(--orange-deep);
  }
  .person__role {
    font-family: "Dosis", sans-serif;
    font-weight: 700;
    font-size: 20px;
    line-height: 1.2;
    color: var(--owner-grey);
  }

  /* Typewriter card */
  .stamp {
    position: absolute;
    left: 53px;
    top: 25px;
    width: 180px;
    height: 187px;
    display: flex;
    flex-direction: column;
    align-items: center;
    justify-content: center;
    gap: 12px;
  }
  .stamp__dot {
    width: 46px;
    height: 46px;
    border-radius: 50%;
    background: var(--red);
  }
  .stamp__name {
    font-family: "Courier Prime", monospace;
    font-weight: 700;
    font-size: 24px;
    line-height: 1.15;
    text-align: center;
    color: var(--red);
  }
  .stamp--ghost {
    left: 428px;
    top: 135px;
    width: 255px;
    height: 255px;
  }
  .stamp--ghost .stamp__dot { width: 70px; height: 70px; background: var(--ghost); }
  .stamp--ghost .stamp__name { font-size: 34px; color: var(--ghost); }
  .ledger {
    position: absolute;
    left: 383px;
    top: 32px;
    display: grid;
    grid-template-columns: 108px auto;
    row-gap: 1px;
    font-family: "Courier Prime", monospace;
    font-weight: 700;
    font-size: 19px;
    line-height: 25px;
    color: var(--mono-ink);
  }
  .signature {
    position: absolute;
    left: 47px;
    top: 276px;
    font-family: "Courier Prime", monospace;
    font-weight: 700;
  }
  .signature__name { font-size: 26px; line-height: 32px; color: var(--mono-name); }
  .signature__role {
    margin-top: 6px;
    margin-left: 96px;
    font-size: 24px;
    line-height: 30px;
    color: var(--mono-role);
  }
</style>
</head>
<body>
<main class="stage">

  <section class="card card--color" aria-label="Business card, colour version">
    <svg class="swoosh" viewBox="0 0 750 412" aria-hidden="true">
      <path d="M330 212 C 470 195, 580 120, 615 0 L 750 0 L 750 30 C 650 110, 500 190, 340 214 Z" fill="var(--orange)"/>
      <path d="M340 214 C 500 192, 650 115, 750 35 L 750 70 C 640 140, 500 200, 350 218 Z" fill="var(--amber)"/>
      <path d="M350 218 C 510 202, 650 145, 750 75 L 750 110 C 650 170, 520 210, 360 222 Z" fill="var(--yellow)"/>
    </svg>
    <div class="brand-mark">
      <span class="brand-mark__dot"></span>
      <span class="brand-mark__name">Tavner's Produce</span>
    </div>
    <div class="tractor" role="img" aria-label="Orange silhouette illustration of a farm tractor"></div>
    <div class="contact">
      <span class="contact__label">Phone</span><span class="contact__value">(509) 555-0147</span>
      <span class="contact__label">Cell</span><span class="contact__value">(509) 555-0183</span>
      <span class="contact__label">Address</span><span class="contact__value">42 Cedar Hollow Ln.</span>
      <span class="contact__label"></span><span class="contact__value">Fernridge, OR 97411</span>
    </div>
    <div class="person">
      <p class="person__name">Marisela Tavner</p>
      <p class="person__role">Owner</p>
    </div>
  </section>

  <section class="card card--type" aria-label="Business card, typewriter version">
    <div class="stamp stamp--ghost" aria-hidden="true">
      <span class="stamp__dot"></span>
      <span class="stamp__name">Tavner's Produce</span>
    </div>
    <div class="stamp">
      <span class="stamp__dot"></span>
      <span class="stamp__name">Tavner's Produce</span>
    </div>
    <div class="ledger">
      <span>Phone</span><span>(509) 555-0147</span>
      <span>Cell</span><span>(509) 555-0183</span>
      <span>Address</span><span>42 Cedar Hollow Ln.</span>
      <span></span><span>Fernridge, OR 97411</span>
    </div>
    <div class="signature">
      <p class="signature__name">Marisela Tavner</p>
      <p class="signature__role">Owner</p>
    </div>
  </section>

</main>
</body>
</html>
```